Business card design needed

I need a business card for my new Food & Lifestyle Coaching business - "Bloomvale Food & Lifestlye Coaching"

i already have a logo and would like to have that incorporated into the business card, obviously.

i would like a design that says "fresh" and "funky" - my target market is female, aged 20-45 so i want something that will stand out to them when they see it.

My "Company Colour" is Apple Green
Updates

Thankyou to everyone who has submitted a design for my project. At this stage i have quite a large number of designs to chose from and with only a short time until my project closes i am focusing now on chosing from those i have already shortlisted so am unfortunately not considering any new desings.

Thankyou again for your interest in my project.

Target Market(s)

Female, Health Conscious (or looking to improve their health/lifestyle), aged between 20-45

Industry/Entity Type

Business

Contact Information for Business Card

Tamsin Corley
Ph: 0417382946
Email: eatwell@marovex.com

Requirements
Must have
• Must include my existing Logo
Nice to have
• Would be nice to incoirporate and appointment card on the back

```html
<!DOCTYPE html>
<html lang="en">
<head>
<meta charset="utf-8">
<title>Bloomvale – Business Card</title>
<link rel="stylesheet" href="https://fonts.googleapis.com/css2?family=Delius&family=Open+Sans:wght@400&display=swap">
<style>
  :root {
    --backdrop: #3b3b3b;
    --apple-green: #8cc63f;
    --green-light: #5d9b3a;
    --green-dark: #2c5220;
    --silver-light: #ffffff;
    --silver-mid: #e4e4e4;
    --silver-dark: #b9b9b9;
    --ink: #1e1e1e;
    --ink-grey: #7a7a7a;
    --label-grey: #333333;
    --white: #ffffff;
  }
  * { box-sizing: border-box; margin: 0; padding: 0; }
  html, body { width: 1200px; height: 900px; overflow: hidden; }
  body { background: var(--backdrop); position: relative; font-family: "Open Sans", Arial, sans-serif; }

  .card {
    position: absolute;
    top: 305px;
    height: 285px;
    border-radius: 26px;
    overflow: hidden;
  }

  /* Front */
  .card-front {
    left: 80px;
    width: 520px;
    background: linear-gradient(180deg, var(--green-light) 0%, var(--green-dark) 100%);
  }
  .card-front .swoosh { position: absolute; inset: 0; width: 100%; height: 100%; }
  .brand {
    position: absolute;
    display: flex;
    align-items: center;
    gap: 10px;
  }
  .brand-dot { width: 34px; height: 34px; border-radius: 50%; background: var(--apple-green); flex: none; }
  .brand-name { font-family: "Delius", cursive; font-size: 50px; line-height: 1; }
  .brand-tagline { position: absolute; font-family: "Open Sans", Arial, sans-serif; font-size: 12px; }

  .card-front .brand { left: 28px; top: 38px; }
  .card-front .brand-name { color: var(--ink); }
  .card-front .brand-tagline { left: 164px; top: 106px; color: var(--ink); }

  .holder-name {
    position: absolute;
    left: 22px; bottom: 30px;
    font-family: "Delius", cursive;
    font-size: 24px;
    color: var(--white);
    letter-spacing: 0.5px;
  }
  .contact { position: absolute; left: 280px; bottom: 22px; color: var(--white); }
  .contact-line { display: flex; align-items: center; gap: 6px; font-size: 13px; height: 19px; }
  .contact-line.phone { letter-spacing: 5px; }
  .contact-line svg { flex: none; }

  /* Back */
  .card-back {
    left: 625px;
    width: 505px;
    background: linear-gradient(160deg, var(--silver-light) 0%, var(--silver-mid) 45%, var(--silver-light) 70%, var(--silver-dark) 100%);
  }
  .appointment-title {
    position: absolute; left: 20px; top: 18px;
    font-family: "Delius", cursive; font-size: 21px; color: var(--label-grey);
  }
  .appointment-field {
    position: absolute; left: 20px;
    display: flex; align-items: flex-end; gap: 4px;
    font-size: 13px; color: var(--label-grey);
  }
  .appointment-field .rule { display: block; height: 1px; background: var(--label-grey); margin-bottom: 3px; }
  .field-date { top: 58px; }
  .field-date .rule { width: 258px; }
  .field-time { top: 100px; }
  .field-time .rule { width: 260px; }

  .card-back .brand { left: 190px; top: 172px; }
  .card-back .brand-name { color: var(--ink-grey); }
  .card-back .brand-tagline { left: 326px; top: 238px; color: var(--ink-grey); }
</style>
</head>
<body>

  <section class="card card-front" aria-label="Business card front">
    <svg class="swoosh" viewBox="0 0 520 285" preserveAspectRatio="none" aria-hidden="true">
      <defs>
        <linearGradient id="silverBand" x1="0" y1="0" x2="1" y2="0">
          <stop offset="0" stop-color="#9a9a9a"/>
          <stop offset="0.5" stop-color="#f2f2f2"/>
          <stop offset="1" stop-color="#8d8d8d"/>
        </linearGradient>
        <linearGradient id="whitePanel" x1="0" y1="0" x2="0" y2="1">
          <stop offset="0" stop-color="#f4f4f4"/>
          <stop offset="1" stop-color="#ffffff"/>
        </linearGradient>
      </defs>
      <path d="M0 0 H478 C440 100 330 176 200 180 C110 183 40 164 0 146 Z" fill="url(#silverBand)"/>
      <path d="M0 0 H468 C430 92 326 164 200 168 C110 171 40 152 0 134 Z" fill="url(#whitePanel)"/>
    </svg>

    <div class="brand">
      <span class="brand-dot"></span>
      <span class="brand-name">Bloomvale</span>
    </div>
    <p class="brand-tagline">Food &amp; Lifestyle Coaching</p>

    <p class="holder-name">Tamsin Corley</p>

    <div class="contact">
      <p class="contact-line phone">
        <svg width="22" height="13" viewBox="0 0 22 13" aria-hidden="true">
          <rect x="1" y="1" width="20" height="11" rx="2" fill="none" stroke="#fff" stroke-width="1.5"/>
          <rect x="4" y="3.5" width="8" height="6" fill="#fff"/>
        </svg>
        0417382946
      </p>
      <p class="contact-line">
        <svg width="20" height="13" viewBox="0 0 20 13" aria-hidden="true">
          <rect x="1" y="1" width="18" height="11" fill="none" stroke="#fff" stroke-width="1.4"/>
          <path d="M1 1 L10 8 L19 1" fill="none" stroke="#fff" stroke-width="1.4"/>
        </svg>
        eatwell@marovex.com
      </p>
    </div>
  </section>

  <section class="card card-back" aria-label="Appointment card back">
    <h2 class="appointment-title">Appointment</h2>
    <p class="appointment-field field-date">Date: <span class="rule"></span></p>
    <p class="appointment-field field-time">Time: <span class="rule"></span></p>

    <div class="brand">
      <span class="brand-dot"></span>
      <span class="brand-name">Bloomvale</span>
    </div>
    <p class="brand-tagline">Food &amp; Lifestyle Coaching</p>
  </section>

</body>
</html>
```